Investment company needing business card

We are wanting a business card which looks sharp and easy on the eye. We are thinking of having a business card with the logo embossed on it, to really make it stand out. We will only have a small amount of information of the business card, person's name, position, email address and phone number

Contact Information for Business Card

Danica Pruett
Executive Assistant
+64 21 547 3162
danicap@harwellcapital.co.nz

Requirements
Must have
• Embossed logo
Should not have
• Not to be busy

```html
<!DOCTYPE html>
<html lang="en">
<head>
<meta charset="utf-8">
<title>Harwell Capital — Business Card</title>
<link href="https://fonts.googleapis.com/css2?family=Michroma&family=Quicksand:wght@500&display=swap" rel="stylesheet">
<style>
  :root {
    --canvas: #e9e7e3;
    --card: #f6f4f0;
    --green: #2fae6c;
    --grey: #5e5e5e;
    --ink: #4a4a4a;
  }
  * { box-sizing: border-box; margin: 0; padding: 0; }
  html, body { width: 800px; height: 1200px; overflow: hidden; }
  body {
    background: var(--canvas);
    position: relative;
    font-family: "Quicksand", sans-serif;
  }
  .card {
    position: absolute;
    left: 60px;
    width: 680px;
    height: 389px;
    background: var(--card);
    box-shadow: 0 6px 18px rgba(0,0,0,0.12);
    overflow: hidden;
  }
  .card--front { top: 160px; }
  .card--back { top: 650px; }

  /* Front */
  .brand {
    position: absolute;
    left: 0; right: 0; top: 120px;
    display: flex;
    flex-direction: column;
    align-items: center;
    gap: 26px;
  }
  .brand__mark {
    width: 64px; height: 64px;
    background: var(--green);
    box-shadow: 1px 2px 2px rgba(0,0,0,0.18);
  }
  .brand__name {
    font-family: "Michroma", sans-serif;
    font-size: 30px;
    letter-spacing: 2px;
    color: var(--green);
    text-transform: uppercase;
    text-shadow: 1px 1px 1px rgba(0,0,0,0.15);
  }

  /* Back */
  .person {
    position: absolute;
    right: 382px;
    top: 170px;
    text-align: right;
    font-family: "Michroma", sans-serif;
    text-transform: uppercase;
  }
  .person__name { font-size: 17px; color: var(--green); letter-spacing: 1px; }
  .person__role { font-size: 10.5px; color: var(--grey); letter-spacing: 2px; margin-top: 6px; }
  .divider {
    position: absolute;
    left: 318px; top: 140px;
    width: 1.5px; height: 84px;
    background: var(--green);
  }
  .contacts {
    position: absolute;
    left: 334px; top: 144px;
    list-style: none;
    font-size: 15px;
    color: var(--ink);
  }
  .contacts li { display: flex; align-items: center; gap: 8px; height: 25px; }
  .contacts svg { width: 15px; height: 15px; flex: none; }
  .band {
    position: absolute;
    left: 0; top: 345px;
    width: 540px; height: 11px;
    background: var(--green);
  }
  .band-mark {
    position: absolute;
    left: 556px; top: 338px;
    width: 24px; height: 24px;
    background: var(--green);
  }
  .band-tail {
    position: absolute;
    left: 596px; top: 345px;
    right: 0; height: 11px;
    background: var(--grey);
  }
</style>
</head>
<body>
  <section class="card card--front">
    <div class="brand">
      <div class="brand__mark"></div>
      <div class="brand__name">Harwell Capital</div>
    </div>
  </section>

  <section class="card card--back">
    <div class="person">
      <div class="person__name">Danica Pruett</div>
      <div class="person__role">Executive Assistant</div>
    </div>
    <div class="divider"></div>
    <ul class="contacts">
      <li>
        <svg viewBox="0 0 16 16"><rect x="1" y="1" width="14" height="14" rx="4" fill="none" stroke="#2fae6c" stroke-width="1.5"/><path d="M5.5 4.5l1.5 0 .8 2-1 .8a5 5 0 0 0 2 2l.8-1 2 .8v1.5c0 .6-.5 1-1 1A7 7 0 0 1 4.5 5.5c0-.5.4-1 1-1z" fill="#2fae6c"/></svg>
        +64 21 547 3162
      </li>
      <li>
        <svg viewBox="0 0 16 16"><rect x="1" y="1" width="14" height="14" rx="4" fill="#2fae6c"/><rect x="4" y="5" width="8" height="6" fill="none" stroke="#fff" stroke-width="1"/><path d="M4 5l4 3.5L12 5" fill="none" stroke="#fff" stroke-width="1"/></svg>
        danicap@harwellcapital.co.nz
      </li>
      <li>
        <svg viewBox="0 0 16 16"><rect x="1" y="1" width="14" height="14" rx="4" fill="#2fae6c"/><circle cx="8" cy="8" r="4" fill="none" stroke="#fff" stroke-width="1"/><path d="M4 8h8M8 4c-2 2.5-2 5.5 0 8M8 4c2 2.5 2 5.5 0 8" fill="none" stroke="#fff" stroke-width="0.9"/></svg>
        www.harwellcapital.co.nz
      </li>
    </ul>
    <div class="band"></div>
    <div class="band-mark"></div>
    <div class="band-tail"></div>
  </section>
</body>
</html>
```